Postcard Design

Name of Company: PRAIRIE LOT BROKERS - A NEW AND RESALE MANUFACTURED HOME COMPANY, AID IN THE PURCHASE OR SELL OF NEW AND USED MOBILEHOMES, HAVE OVER 30 YEARS IN THE REAL ESTATE INDUSTRY,
WE OFFER A FREE HOME INSPECTION WITH EVERY NEW LISTING A $250.00 VALUE SO YOU KNOW THE HEALTH AND SAFETY STATUS OF YOUR HOME SO THERE ARE NO SURPRISES WHEN YOU ARE READY TO CLOSE THE SALE OF YOUR HOME AND HAVE TO GIVE UP THOUSANDS OF DOLLARS IN REPAIRS.

"COUPON" GOOD FOR $2,000.00 OFF SALES COMMISSION
WE BUY MOBILEHOMES

Check out our site for more information:
prairielotbrokers.com

Target Market(s)

MOBILEHOME OWNERS/ BUYERS

Industry/Entity Type

Real Estate

Colors
00a990
00a98f
86cfc6
33a6d7
3276b5

Requirements
Must have
• CAN WE USE TWO SIDES OF POST CARD

```html
<!DOCTYPE html>
<html lang="en">
<head>
<meta charset="utf-8">
<title>Prairie Lot Brokers – Postcard</title>
<link rel="stylesheet" href="https://fonts.googleapis.com/css2?family=Lato:ital,wght@0,300;1,700&family=Roboto:wght@300&family=Roboto+Condensed:wght@400;700&display=swap">
<style>
  :root {
    --paper: #ffffff;
    --ink: #111111;
    --headline-red: #d5181f;
    --brand-blue: #3c8de0;
    --text-blue: #3a8bd8;
    --offer-yellow: #f7e51b;
    --coupon-yellow: #fdf300;
    --coupon-red: #d8141b;
    --navy: #1f3b7a;
    --rule-grey: #555555;
  }
  * { margin: 0; padding: 0; box-sizing: border-box; }
  html, body { width: 1200px; height: 924px; overflow: hidden; background: var(--paper); }
  .postcard { position: relative; width: 1200px; height: 924px; background: var(--paper); overflow: hidden; }

  .headline-top {
    position: absolute; left: 42px; top: 34px;
    font: 300 82px/1 "Lato", sans-serif; color: var(--ink); letter-spacing: -1px;
  }
  .headline-bottom {
    position: absolute; left: 290px; top: 124px; white-space: nowrap;
    font: italic 700 80px/1 "Lato", sans-serif; color: var(--headline-red); letter-spacing: 2px;
  }
  .header-divider {
    position: absolute; left: 859px; top: 44px; height: 152px;
    border-left: 2px dotted var(--rule-grey);
  }
  .experience {
    position: absolute; left: 900px; top: 86px; width: 280px;
    font: 400 28px/1.28 "Roboto Condensed", sans-serif; color: var(--text-blue);
  }
  .experience strong { font-weight: 700; }

  .service-band {
    position: absolute; left: 0; top: 252px; width: 775px; height: 260px;
    background: var(--brand-blue);
  }
  .edge-strip {
    position: absolute; left: 1157px; top: 252px; width: 43px; height: 260px;
    background: var(--brand-blue);
  }
  .service-intro {
    position: absolute; left: 44px; top: 270px; width: 540px; white-space: nowrap;
    font: 300 27px/36px "Roboto", sans-serif; color: var(--paper);
  }
  .band-rule {
    position: absolute; left: 44px; top: 395px; width: 528px;
    border-top: 2px dotted rgba(255,255,255,0.8);
  }
  .inspection-offer {
    position: absolute; left: 44px; top: 414px; width: 545px; white-space: nowrap;
    font: 700 35px/42px "Roboto Condensed", sans-serif; color: var(--offer-yellow); letter-spacing: 0.6px;
  }
  .home-gallery {
    position: absolute; left: 593px; top: 262px; width: 170px; height: 238px;
    background: linear-gradient(160deg, #c9cfd6 0%, #8f8a80 45%, #6a5a4c 75%, #7c8f5a 100%);
    border: 5px solid var(--paper);
  }
  .family-photo {
    position: absolute; left: 770px; top: 240px; width: 388px; height: 684px;
    background: linear-gradient(180deg, #f4f4f2 0%, #e9dcd0 35%, #f1d9dc 70%, #f6eef0 100%);
  }

  .body-copy {
    position: absolute; top: 524px;
    font: 400 26.5px/36.6px "Roboto Condensed", sans-serif;
  }
  .body-copy span { display: block; white-space: nowrap; text-align: justify; text-align-last: justify; }
  .body-copy span.last { text-align-last: left; }
  .inspection-detail { left: 44px; width: 406px; color: var(--ink); }
  .support-promise { left: 497px; width: 243px; color: var(--text-blue); }
  .support-promise .tight { letter-spacing: -0.6px; word-spacing: -3px; }
  .copy-divider {
    position: absolute; left: 474px; top: 530px; height: 172px;
    border-left: 2px dotted var(--rule-grey);
  }

  .coupon {
    position: absolute; left: 44px; top: 724px; width: 405px; height: 118px;
    background: var(--coupon-yellow); border: 6px dashed var(--ink);
    display: flex; align-items: center; justify-content: center; text-align: center;
    font: 700 32px/40px "Roboto Condensed", sans-serif; color: var(--coupon-red);
  }

  .brand {
    position: absolute; left: 500px; top: 762px;
    display: flex; align-items: center; gap: 10px; white-space: nowrap;
  }
  .brand-mark { width: 22px; height: 22px; background: var(--navy); flex: none; }
  .brand-name {
    font: 700 25px/1.1 "Roboto Condensed", sans-serif; color: var(--navy);
  }

  .tagline {
    position: absolute; left: 44px; top: 858px; white-space: nowrap; z-index: 2;
    font: 400 23px/1 "Roboto Condensed", sans-serif; color: var(--text-blue); letter-spacing: -0.3px;
  }
</style>
</head>
<body>
<main class="postcard">
  <h1>
    <span class="headline-top">Opening Doors</span>
    <span class="headline-bottom">To A Better Life</span>
  </h1>
  <div class="header-divider"></div>
  <p class="experience">Over <strong>30 YEARS</strong> in the<br><strong>REAL ESTATE</strong> industry</p>

  <div class="service-band"></div>
  <div class="edge-strip"></div>
  <p class="service-intro">A New and Resale Manufactured Home<br>Company, aid in the Purchase or Sell of<br>New and Used Mobile Homes</p>
  <div class="band-rule"></div>
  <p class="inspection-offer">We offer a FREE HOME INSPECTION<br>with every new listing a $250 value</p>
  <div class="home-gallery" role="img" aria-label="Collage of manufactured home exterior and interior rooms"></div>

  <div class="family-photo" role="img" aria-label="Mother hugging her young daughter, who holds a pink paper heart"></div>

  <p class="body-copy inspection-detail">
    <span>So you know the health and safety</span>
    <span>status of your home so there are no</span>
    <span>surprises when you are ready to close</span>
    <span>the sale of your home and have to give</span>
    <span class="last">up thousands of dollars in repairs.</span>
  </p>
  <div class="copy-divider"></div>
  <p class="body-copy support-promise">
    <span class="tight">Whether you are buying</span>
    <span>or selling, we will be</span>
    <span>by your side from the</span>
    <span>first consultation to</span>
    <span class="last">the close of escrow.</span>
  </p>

  <div class="coupon">GOOD FOR $2,000.00<br>OFF SALES COMMISSION</div>

  <div class="brand">
    <span class="brand-mark"></span>
    <span class="brand-name">PRAIRIE LOT BROKERS</span>
  </div>

  <p class="tagline">We are energetic, enthusiastic and excited to find the right buyer for your home</p>
</main>
</body>
</html>
```